No Credit Check Financing Sign for the best tire shop on earth.

We need a catchy sign for financing for a tire dealer, size: 4 feet vertical by 8 feet horizontal. The color scheme is red, grey, white, and red. As seen in the logo attached.

No Credit Check Financing.
For Rims And tires
Apply Today online or in store
WWW.morlenwheelhub.com
(505)614-3082

That is the just of what the sign needs to say, feel free to reword and make awesome. Logo needs to appear on sign, as well as phone number and email.

Target Market(s)

Low income. Custom car market for wheel and tire packages. Custom lift kits and car upgrades.

Industry/Entity Type

Shop

Colors
ec1f27
ffffff
eaeaea
000000

Requirements
Must have
• Phone. Logo. Website. awesomeness
Nice to have
• catchy saying, modern look

```html
<!DOCTYPE html>
<html lang="en">
<head>
<meta charset="utf-8">
<title>No Credit Check Financing – Morlen Wheel Hub</title>
<link href="https://fonts.googleapis.com/css2?family=Montserrat:wght@600;700;800;900&display=swap" rel="stylesheet">
<style>
  :root {
    --brand-red: #d0141f;
    --brand-red-deep: #a80f18;
    --white: #ffffff;
    --light-grey: #eaeaea;
    --ink: #222222;
    --tread: #2a2a2a;
  }
  html, body {
    margin: 0;
    padding: 0;
    width: 1200px;
    height: 601px;
    overflow: hidden;
    background: var(--white);
  }
  .sign {
    position: relative;
    width: 1200px;
    height: 601px;
    overflow: hidden;
    font-family: "Montserrat", Arial, sans-serif;
    background: var(--white);
  }
  .sign__field {
    position: absolute;
    left: 0;
    top: 0;
    width: 1200px;
    height: 494px;
    background: var(--brand-red);
  }
  .sign__phone {
    position: absolute;
    left: 77px;
    top: 36px;
    margin: 0;
    font-size: 42px;
    font-weight: 700;
    color: var(--white);
    letter-spacing: 0.5px;
    line-height: 1;
  }
  .sign__tread {
    position: absolute;
    left: 450px;
    top: 40px;
    width: 730px;
    height: 36px;
    background: linear-gradient(90deg, rgba(42,42,42,0.6), var(--tread) 10%, var(--tread) 88%, rgba(42,42,42,0.5));
  }
  .sign__headline {
    position: absolute;
    left: 74px;
    top: 112px;
    margin: 0;
    color: var(--white);
    font-weight: 800;
    line-height: 1;
  }
  .sign__headline-top {
    display: block;
    font-size: 107px;
    letter-spacing: -1px;
  }
  .sign__headline-main {
    display: block;
    margin-top: 6px;
    font-size: 183px;
    letter-spacing: -3px;
  }
  .sign__sub {
    position: absolute;
    left: 78px;
    top: 398px;
    margin: 0;
    font-size: 53px;
    font-weight: 800;
    color: var(--ink);
    line-height: 1;
    letter-spacing: 0.5px;
  }
  .sign__web {
    position: absolute;
    left: 78px;
    top: 518px;
    margin: 0;
    font-size: 40px;
    font-weight: 700;
    color: var(--ink);
    line-height: 1;
  }
  .sign__badge {
    position: absolute;
    left: 740px;
    top: 368px;
    width: 470px;
    height: 240px;
  }
  .sign__brand {
    position: absolute;
    left: 790px;
    top: 468px;
    width: 370px;
    margin: 0;
    text-align: center;
    font-size: 40px;
    font-weight: 900;
    line-height: 1.05;
    color: var(--brand-red);
    text-transform: uppercase;
  }
</style>
</head>
<body>
  <div class="sign">
    <div class="sign__field"></div>

    <p class="sign__phone">(505)614-3082</p>
    <div class="sign__tread" role="img" aria-label="Tire tread track running across the top"></div>

    <h1 class="sign__headline">
      <span class="sign__headline-top">NO CREDIT CHECK</span>
      <span class="sign__headline-main">FINANCING</span>
    </h1>

    <p class="sign__sub">FOR RIMS AND TIRES</p>
    <p class="sign__web">www.morlenwheelhub.com</p>

    <svg class="sign__badge" viewBox="0 0 470 240" aria-hidden="true">
      <circle cx="234" cy="266" r="234" fill="var(--brand-red-deep)"/>
      <circle cx="232" cy="268" r="228" fill="var(--white)"/>
    </svg>
    <p class="sign__brand">Morlen<br>Wheel Hub</p>
  </div>
</body>
</html>
```